Dalton Power Supply, Inc. Business Card Design

We are an Electrical Distributor looking for a Modern, Professional Business Card design.

Target Market(s)

Residential Commercial Industrial

Industry/Entity Type

Electrical

Contact Information for Business Card

Dalton Power Supply, Inc.
418 Maple Ridge Lane
Brookvale, NC 27514
555-214-7630
555-214-8842 Fax
daltonpower@brightmail-example.net

```html
<!DOCTYPE html>
<html lang="en">
<head>
<meta charset="utf-8">
<title>Dalton Power Supply, Inc. Business Card</title>
<link rel="stylesheet" href="https://fonts.googleapis.com/css2?family=Open+Sans:wght@400;600&display=swap">
<style>
  :root {
    --backdrop: #e9e6e2;
    --card-white: #ffffff;
    --card-black: #000000;
    --brand-red: #d9261c;
    --ink: #333333;
    --ring-dark: #444444;
    --ring-light: #6a6a6a;
    --rule: #555555;
  }
  * { margin: 0; padding: 0; box-sizing: border-box; }
  html, body {
    width: 1200px; height: 1000px; overflow: hidden;
    background: var(--backdrop);
    font-family: "Open Sans", Arial, sans-serif;
  }
  .canvas { position: relative; width: 1200px; height: 1000px; }
  .card {
    position: absolute; left: 265px; width: 666px; height: 397px;
    box-shadow: 0 4px 12px rgba(0,0,0,0.25);
  }
  .card--front { top: 73px; background: var(--card-white); }
  .card--back { top: 532px; background: var(--card-black); }

  .brand { position: absolute; display: flex; align-items: center; }
  .brand__ring { border-radius: 50%; flex: none; }
  .brand__name {
    color: var(--brand-red); font-weight: 600; line-height: 1.05;
    text-transform: uppercase; letter-spacing: 0.5px;
  }
  .card--front .brand { left: 33px; top: 33px; }
  .card--front .brand__ring { width: 114px; height: 114px; border: 4px solid var(--ring-dark); }
  .card--front .brand__name { font-size: 30px; margin-left: 14px; }
  .card--back .brand { left: 110px; top: 121px; }
  .card--back .brand__ring { width: 156px; height: 156px; border: 4px solid var(--ring-light); }
  .card--back .brand__name { font-size: 42px; margin-left: 20px; }

  .person { position: absolute; left: 33px; top: 212px; }
  .person__name { color: var(--brand-red); font-size: 20px; font-weight: 600; }
  .person__title { color: var(--ink); font-size: 15px; margin-top: 2px; }

  .divider { position: absolute; left: 33px; right: 33px; top: 277px; border-top: 1.5px solid var(--rule); }

  .contacts { position: absolute; left: 33px; top: 296px; list-style: none; }
  .contacts li {
    display: flex; align-items: center; color: var(--ink);
    font-size: 16px; height: 24.5px;
  }
  .contacts svg { width: 14px; height: 14px; margin-right: 8px; fill: var(--brand-red); }

  .address { position: absolute; right: 33px; top: 295px; text-align: right; font-style: normal; }
  .address__company { color: var(--brand-red); font-size: 15px; font-weight: 600; margin-bottom: 6px; }
  .address__line { color: var(--ink); font-size: 16px; line-height: 22px; }
</style>
</head>
<body>
<main class="canvas">
  <section class="card card--front">
    <div class="brand">
      <span class="brand__ring"></span>
      <span class="brand__name">Dalton Power<br>Supply, Inc.</span>
    </div>

    <div class="person">
      <p class="person__name">Dalton Hayes</p>
      <p class="person__title">Owner / Founder</p>
    </div>

    <div class="divider"></div>

    <ul class="contacts">
      <li>
        <svg viewBox="0 0 16 16" aria-hidden="true"><path d="M1 5c0-2 3-3 7-3s7 1 7 3v1h-3V4.5C11 4 9.5 3.8 8 3.8S5 4 4 4.5V6H1z M3 7h10l1.5 6h-13z M6 9h4v2H6z"/></svg>
        <span>555-214-7630</span>
      </li>
      <li>
        <svg viewBox="0 0 16 16" aria-hidden="true"><path d="M4 1h8v4H4z M1 6h14v6h-3v-2H4v2H1z M5 11h6v4H5z"/></svg>
        <span>555-214-8842</span>
      </li>
      <li>
        <svg viewBox="0 0 16 16" aria-hidden="true"><path d="M1 3h14v1.5L8 9 1 4.5z M1 6l7 4.5L15 6v7H1z"/></svg>
        <span>daltonpower@brightmail-example.net</span>
      </li>
    </ul>

    <address class="address">
      <p class="address__company">Dalton Power Supply, Inc.</p>
      <p class="address__line">418 Maple Ridge Lane</p>
      <p class="address__line">Brookvale, NC 27514</p>
    </address>
  </section>

  <section class="card card--back">
    <div class="brand">
      <span class="brand__ring"></span>
      <span class="brand__name">Dalton Power<br>Supply, Inc.</span>
    </div>
  </section>
</main>
</body>
</html>
```